Thornbury Cleaning – Website Redesign (Clean, Modern, Trust-Focused)

Thornbury Cleaning — Homepage Redesign Brief

Project Goal

We need a complete redesign of the homepage for our cleaning business, Thornbury Cleaning.
The goal is a clean, modern, trust-building homepage that works equally well for:
• Residential clients
• Commercial clients

The page should feel polished, reliable, easy to navigate, and completely free from clutter, gimmicks, or corporate-sounding fluff.

About Us (Context)

Thornbury Cleaning has operated in Sale, Victoria for over 30 years.
Our brand is built on:
• Reliability
• Convenience
• Long-term trust
• Straightforward, no-nonsense communication

We do not want to look like a large franchise, and we do not want to look cute or playful.
The design must feel modern, practical, confident, and professional.

What We Need Designed — Homepage Only

1. Hero Section

A clean, modern hero area with:
• A simple image or clean background (no clutter, no heavy overlays).
Images from our current site may be helpful, or you may source alternatives.
• Headline suggestion (designer may refine):
“30+ Years of Commercial and Residential Cleaning in Sale”
• Sub-headline suggestion:
“Trusted by locals for three decades.”
• Primary CTA button: Get a Quote

2. Trust-Building Logos

Positioned directly beneath the hero:
• Small, neat logos of organisations we work with
(RLK, Bramwell, Eastvale Regional Care, OPM, etc.)
• A clean Reviewly Reviews block (stars + review count)
• Must be compact, tidy, evenly spaced — not loud or oversized

3. Trust Block / Problem–Solution Copy

This section introduces why hiring cleaners can be stressful and why reliability matters.

Headline example:
“Call the cleaners you can count on.”

We have existing copy for this section.
Please present it in a minimal, breathable, modern layout that is easy to scan.

4. Stats / Counters Section

Three sharp, structured stat boxes:
• 92+ Recurring Clients
• 4,150+ Visits Per Year
• 265+ Pre-Sale / Exit Cleans

These should look clean and understated — not oversized or gimmicky.

5. Values Section

A short section featuring our core values:
• Be Real
• Do It Right
• Have Fun
• Make It Easy

Designer has flexibility with layout.
(Sections 5 and 6 may swap depending on what flows better.)

6. Services Preview

A simple grid or row with links to our main services:
• Commercial Cleaning
• Residential Cleaning
• Window Cleaning
• Steam Cleaning

Small icons or photos are fine — but no clip art or cartoon-style graphics.

7. Footer

A very clean, simple footer with contact details.
No clutter, no heavy visual styling.

Style Requirements

Overall Tone
• Clean
• Modern
• Minimal
• Trust-driven
• Easy to read and navigate

Do NOT use
• Clip art
• Cute or playful icons
• Flowers, sparkles, “feminine” cleaning imagery
• Heavy or overly bold corporate fonts
• Busy backgrounds
• Long paragraphs of text

Reference Material

Current Website (for copy + structure only)

https://thornburycleaning-example.com.au

Rough Canva Mock-Up (layout inspiration only)

(We will upload this separately. It’s not a final design — just a loose concept for spacing/flow.)

Logo

Please use the new Thornbury Cleaning logo (uploaded in files) or a placeholder if needed. Attached is a potential for a new logo or site colours not wedded to the idea though.

What the Homepage Should Communicate

Within seconds, a visitor should understand that:
• We are established
• We are local
• We are reliable
• We make cleaning easy
• Getting a quote is quick and simple

The homepage should feel effortless, trustworthy, and modern.

Deliverable

A complete homepage design layout suitable for WordPress.
Figma, Adobe XD, or a similar design tool is fine.

Target Market(s)

Residential and commercial clients in Sale, Victoria and surrounding Gippsland region. Typical clients include busy households, office managers, receptionists, medical centres, community organisations, local businesses, and real estate/property professionals. Clients value reliability, simplicity, and stress-free long-term cleaning support.

Industry/Entity Type

Cleaning services (Residential & Commercial)

Font styles to use
Sans Serif

Requirements
Must have
• • Clean, modern, minimal layout • A trust-driven design that highlights proof (logos, stats, reviews) near the top • Clear hierarchy and no clutter • A strong hero section with simple messaging and a clear CTA • Trust logos + Reviewly Reviews block directly under the hero • Structured stats/counters section • Values section (Be Real, Do It Right, Have Fun, Make It Easy) • Services preview (Commercial, Residential, Window, Steam/Carpet) • Clean footer with contact details • Use our new Thornbury Cleaning logo (or placeholder if needed) • Easy-to-read typography and spacing • Must feel like a local, real cleaning business — not a franchise
Nice to have
• • An option with centred hero text and an option with left-aligned text • Option to preview hero section with or without a quote form • Subtle use of the navy + gold palette (not heavy or corporate) • Soft, minimal background images (not busy city skylines) • Subtle section dividers or whitespace breaks to improve flow • Slightly rounded card corners for a friendly but still modern feel
Should not have
• • No clip-art, cartoon mops, sparkles, bubbles, or generic cleaning icons • No overly bold, blocky, or corporate fonts • No “mega-city” skylines (we are a regional/rural business) • No heavy overlays, dark gradients, or cluttered hero images • No long paragraphs or dense text blocks • No template-style designs that look generic or AI-generated • No overly feminine, overly masculine, or overly playful designs • No neon colors or high-saturation palettes

```html
<!DOCTYPE html>
<html lang="en">
<head>
<meta charset="utf-8">
<title>Thornbury Cleaning – Homepage</title>
<link href="https://fonts.googleapis.com/css2?family=Poppins:wght@400;500;600;700;800&display=swap" rel="stylesheet">
<style>
:root{
  --navy:#15305a;
  --navy-dark:#0f2547;
  --gold:#b07a1f;
  --gold-light:#c99236;
  --ink:#1d1d1f;
  --muted:#5d6470;
  --line:#e6e8ec;
  --soft:#f3f4f6;
  --white:#ffffff;
}
*{box-sizing:border-box;margin:0;padding:0}
html,body{width:1200px;height:3212px;overflow:hidden}
body{font-family:"Poppins",sans-serif;color:var(--ink);background:var(--white);position:relative}
.btn{display:inline-block;background:var(--gold);color:var(--white);font-weight:600;font-size:13px;border-radius:22px;padding:10px 22px;text-decoration:none}

/* Hero */
.hero{position:relative;height:780px;overflow:hidden}
.hero-photo{position:absolute;inset:0;background:linear-gradient(180deg,#5b86b8 0%,#8fb3d6 28%,#c9d7e0 46%,#8a7a66 62%,#6e6552 76%,#5f7a46 90%,#4d6b36 100%)}
.hero-shade{position:absolute;inset:0;background:linear-gradient(180deg,rgba(15,37,71,.35) 0%,rgba(15,37,71,0) 45%)}
.nav{position:absolute;top:22px;left:60px;right:60px;display:flex;align-items:center;justify-content:space-between}
.brand{color:var(--white);text-align:center;line-height:1}
.brand-name{font-weight:800;font-size:26px;letter-spacing:.5px}
.brand-sub{font-weight:700;font-size:13px;letter-spacing:5px;margin-top:3px}
.brand-est{font-size:8px;letter-spacing:2px;margin-top:4px}
.nav-links{display:flex;align-items:center;gap:30px;list-style:none}
.nav-links a{color:var(--white);font-size:13px;text-decoration:none;font-weight:500}
.hero-copy{position:absolute;top:160px;left:0;right:0;text-align:center;color:var(--white)}
.hero-kicker{font-size:36px;font-weight:600}
.hero-title{font-size:56px;font-weight:700;line-height:1.15}
.hero-sub{font-size:14px;margin-top:10px}
.hero-copy .btn{margin-top:34px}
.scroll-mark{position:absolute;left:50%;bottom:-1px;transform:translateX(-50%);width:84px;height:54px;background:var(--white);border-radius:42px 42px 0 0;display:flex;justify-content:center;padding-top:12px}
.scroll-mark span{width:20px;height:30px;border:2px solid var(--gold-light);border-radius:10px}

/* Partner logos */
.partners{height:300px;display:flex;justify-content:center;align-items:center;gap:40px}
.partner{width:130px;height:130px;border-radius:50%;background:var(--white);box-shadow:0 6px 22px rgba(0,0,0,.1);display:flex;align-items:center;justify-content:center;text-align:center;font-weight:600;font-size:15px;color:var(--navy);padding:14px;line-height:1.25}

/* Values */
.values{height:250px;text-align:center}
.section-title{font-size:30px;font-weight:600;color:var(--ink)}
.values-row{display:flex;justify-content:center;margin-top:48px}
.value{width:225px;padding:0 14px;border-right:1px solid var(--line)}
.value:last-child{border-right:none}
.value h3{font-size:16px;font-weight:600}
.value p{font-size:11px;color:var(--muted);margin-top:4px}

/* Trust block */
.trust{height:420px;display:flex;gap:48px;padding:40px 0 0 130px;border-top:1px solid var(--line)}
.trust-photo{width:330px;height:300px;border-radius:6px;background:linear-gradient(135deg,#cfd6dc 0%,#9aa7b2 45%,#3f4f61 100%)}
.trust-copy{width:480px;padding-top:18px}
.trust-copy h2{font-size:30px;font-weight:700;line-height:1.2;color:var(--ink)}
.trust-copy p{font-size:11.5px;color:var(--muted);margin-top:12px;line-height:1.55}
.trust-copy strong{color:var(--ink)}

/* Stats */
.stats{height:470px;background:var(--soft);display:flex;justify-content:center;align-items:center;gap:24px}
.stat{width:250px;height:270px;background:var(--white);border-radius:8px;box-shadow:0 4px 14px rgba(0,0,0,.06);text-align:center;padding:28px 24px}
.stat-icon{width:64px;height:64px;border-radius:50%;background:var(--gold);margin:0 auto;display:flex;align-items:center;justify-content:center}
.stat h3{font-size:16px;font-weight:600;margin-top:16px}
.stat .num{font-size:34px;font-weight:700;color:var(--navy);line-height:1.3}
.stat p{font-size:11px;color:var(--muted);line-height:1.5}

/* Services */
.services{height:580px;text-align:center;padding-top:80px;position:relative}
.service-row{display:flex;justify-content:center;gap:20px;margin-top:40px}
.service{width:460px}
.service-photo{height:240px;border-radius:6px}
.service-photo.commercial{background:linear-gradient(135deg,#e9ecef 0%,#b8c1c9 50%,#56606c 100%)}
.service-photo.residential{background:linear-gradient(135deg,#f1ece4 0%,#c9b9a1 45%,#2f4d72 100%)}
.service h3{font-size:16px;font-weight:600;margin-top:22px}
.service p{font-size:11px;color:var(--muted);margin-top:4px}
.service .btn{margin-top:16px;font-size:11px;padding:8px 20px}
.arrow{position:absolute;top:260px;width:40px;height:40px;border-radius:50%;background:var(--navy);display:flex;align-items:center;justify-content:center}
.arrow.prev{left:80px}.arrow.next{right:80px}

/* Footer */
.footer{height:350px;background:var(--navy);color:var(--white);display:flex;padding:70px 0 0 130px;gap:0}
.footer .brand{width:340px;text-align:left}
.footer .brand-name{font-size:38px}
.footer .brand-sub{font-size:19px;letter-spacing:8px}
.footer .brand-est{font-size:11px}
.footer-col{width:360px}
.footer-col h4{font-size:18px;font-weight:600;margin-bottom:18px}
.contact-list{list-style:none}
.contact-list li{display:flex;align-items:center;gap:10px;font-size:11px;margin-bottom:10px}
.cards{display:flex;gap:8px}
.card{width:52px;height:32px;background:var(--white);border-radius:4px;color:var(--navy);font-size:9px;font-weight:600;display:flex;align-items:center;justify-content:center}
.seal{width:64px;height:64px;border-radius:50%;background:var(--white);margin-top:18px}
.bottom-bar{height:62px;background:var(--navy-dark);color:var(--white);font-size:11px;letter-spacing:1px;display:flex;align-items:center;justify-content:center;position:relative}
.to-top{position:absolute;right:36px;top:14px;width:34px;height:34px;border-radius:50%;background:var(--gold);display:flex;align-items:center;justify-content:center}
</style>
</head>
<body>

<header class="hero">
  <div class="hero-photo" role="img" aria-label="Photo of a two-storey suburban house with a green lawn under a blue sky"></div>
  <div class="hero-shade"></div>
  <nav class="nav">
    <div class="brand">
      <div class="brand-name">THORNBURY</div>
      <div class="brand-sub">CLEANING</div>
      <div class="brand-est">EST. 1990</div>
    </div>
    <ul class="nav-links">
      <li><a href="#">Home</a></li>
      <li><a href="#">About Us</a></li>
      <li><a href="#">Our Service</a></li>
      <li><a href="#">Contact Us</a></li>
      <li><a class="btn" href="#">Get A Quote</a></li>
    </ul>
  </nav>
  <div class="hero-copy">
    <div class="hero-kicker">30+ Years of Commercial And</div>
    <h1 class="hero-title">Residential Cleaning in Sale</h1>
    <p class="hero-sub">Trusted by locals for three decades.</p>
    <a class="btn" href="#">Get A Quote</a>
  </div>
  <div class="scroll-mark"><span></span></div>
</header>

<section class="partners">
  <div class="partner">RLK</div>
  <div class="partner">Bramwell</div>
  <div class="partner">Eastvale Regional Care</div>
  <div class="partner">OPM</div>
  <div class="partner">Reviewly Reviews<br>★★★★★</div>
</section>

<section class="values">
  <h2 class="section-title">Core Values</h2>
  <div class="values-row">
    <div class="value"><h3>Be Real</h3><p>Honest and straightforward every single visit</p></div>
    <div class="value"><h3>Do It Right</h3><p>We always do everything the proper way</p></div>
    <div class="value"><h3>Have Fun</h3><p>Enjoy the process, new and easy</p></div>
    <div class="value"><h3>Make It Easy</h3><p>We make cleaning simple</p></div>
  </div>
</section>

<section class="trust">
  <div class="trust-photo" role="img" aria-label="Photo of a cleaner in a uniform wiping a large window"></div>
  <div class="trust-copy">
    <h2>Call the cleaners You can<br>count on</h2>
    <p>When you need help cleaning, the last thing you need is more stress. Too often, that's exactly what happens –</p>
    <p>Cleaners don't show up, rooms get missed or half done, and you're left <strong>wondering why you didn't just do it yourself.</strong></p>
    <p>You shouldn't have to second-guess whether the job will be done right.</p>
    <p>You should be able to <strong>book it, forget it, and trust it's sorted</strong> properly.</p>
    <p><strong>Trusted by locals for 30+ years</strong> to deliver reliable, long-term cleaning that frees your time for what matters.</p>
  </div>
</section>

<section class="stats">
  <div class="stat">
    <div class="stat-icon"><svg width="30" height="30" viewBox="0 0 30 30" fill="none" stroke="#fff" stroke-width="2.2"><circle cx="15" cy="10" r="5"/><path d="M5 26c1-6 5-9 10-9s9 3 10 9"/></svg></div>
    <h3>Recurring Clients</h3>
    <div class="num">92+</div>
    <p>Homes, offices and medical centres that rely on us each week.</p>
  </div>
  <div class="stat">
    <div class="stat-icon"><svg width="30" height="30" viewBox="0 0 30 30" fill="none" stroke="#fff" stroke-width="2.2"><rect x="4" y="7" width="22" height="19" rx="2"/><path d="M4 13h22M10 4v6M20 4v6"/></svg></div>
    <h3>Visits Per Year</h3>
    <div class="num">4,150+</div>
    <p>That's hundreds of homes and workplaces cleaned across Sale each month.</p>
  </div>
  <div class="stat">
    <div class="stat-icon"><svg width="30" height="30" viewBox="0 0 30 30" fill="none" stroke="#fff" stroke-width="2.2"><path d="M4 14L15 5l11 9M7 12v13h16V12"/><path d="M12 25v-7h6v7"/></svg></div>
    <h3>Pre-sale/Exit Cleans</h3>
    <div class="num">265+</div>
    <p>Move-out and pre-sale cleans that help properties shine.</p>
  </div>
</section>

<section class="services">
  <h2 class="section-title">Thornbury Cleaning Services</h2>
  <a class="arrow prev" href="#" aria-label="Previous"><svg width="14" height="14" viewBox="0 0 14 14"><path d="M9 2L4 7l5 5" fill="none" stroke="#fff" stroke-width="2"/></svg></a>
  <div class="service-row">
    <div class="service">
      <div class="service-photo commercial" role="img" aria-label="Photo of a cleaning team working in an office"></div>
      <h3>Commercial Cleaning</h3>
      <p>Keep your workplace fresh with reliable scheduled care.</p>
      <a class="btn" href="#">Read More</a>
    </div>
    <div class="service">
      <div class="service-photo residential" role="img" aria-label="Photo of cleaners tidying a bright living room"></div>
      <h3>Residential Cleaning</h3>
      <p>Enjoy the freedom of a spotless home without stress.</p>
      <a class="btn" href="#">Read More</a>
    </div>
  </div>
  <a class="arrow next" href="#" aria-label="Next"><svg width="14" height="14" viewBox="0 0 14 14"><path d="M5 2l5 5-5 5" fill="none" stroke="#fff" stroke-width="2"/></svg></a>
</section>

<footer class="footer">
  <div class="brand">
    <div class="brand-name">THORNBURY</div>
    <div class="brand-sub">CLEANING</div>
    <div class="brand-est">EST. 1990</div>
  </div>
  <div class="footer-col">
    <h4>Thornbury Cleaning</h4>
    <ul class="contact-list">
      <li><svg width="12" height="12" viewBox="0 0 12 12"><path d="M2 1h3l1 3-1.5 1a7 7 0 0 0 2.5 2.5L8 6l3 1v3a1 1 0 0 1-1 1A9 9 0 0 1 1 2a1 1 0 0 1 1-1z" fill="#fff"/></svg>Phone: 0400 000 111</li>
      <li><svg width="12" height="12" viewBox="0 0 12 12" fill="none" stroke="#fff"><rect x="1" y="2.5" width="10" height="7" rx="1"/><path d="M1 3l5 4 5-4"/></svg>Email: info@thornburycleaning-example.com.au</li>
      <li><svg width="12" height="12" viewBox="0 0 12 12"><circle cx="6" cy="6" r="5" fill="none" stroke="#fff"/></svg>ABN: 00 000 000 000</li>
      <li><svg width="12" height="12" viewBox="0 0 12 12" fill="none" stroke="#fff"><circle cx="6" cy="6" r="5"/><path d="M6 3v3l2 1"/></svg>Hours: Monday – Friday 9am–5pm</li>
      <li><svg width="12" height="12" viewBox="0 0 12 12"><path d="M6 1a3.5 3.5 0 0 0-3.5 3.5C2.5 7 6 11 6 11s3.5-4 3.5-6.5A3.5 3.5 0 0 0 6 1z" fill="#fff"/></svg>Address: 8 Wattle Lane, Sale VIC 3850</li>
    </ul>
  </div>
  <div class="footer-col">
    <h4>Payment</h4>
    <div class="cards">
      <div class="card">Paywise</div>
      <div class="card">Cardly</div>
      <div class="card">Tapgo</div>
      <div class="card">Bankr</div>
    </div>
    <div class="seal"></div>
  </div>
</footer>
<div class="bottom-bar">©2000–2025 THORNBURY CLEANING
  <a class="to-top" href="#" aria-label="Back to top"><svg width="12" height="12" viewBox="0 0 12 12"><path d="M2 8l4-4 4 4" fill="none" stroke="#fff" stroke-width="2"/></svg></a>
</div>

</body>
</html>
```